Business Card for Quillmark Ledger - A cannabis publication for executives.

I'd like some business cards for Quillmark Ledger. The logo is done (great job!) and I need a card design I will use with PRINTLY. I made it a short project to allow time for printing before an event. These will be standard sized cards (final artwork size 3.66" x 2.16" at 300dpi) with a final card size of 3.5" x 2.0". (See PRINTLY.com if you need more info.) I might try rounded corners but am not sure yet. I think the design will work okay with rounded.

Quillmark Ledger will be a bi-weekly publication for the cannabis industry. It is targeted to investors and industry executives, not consumers or pot smokers. So our market is more B2B. However I am open to creativity and making the card something people remark on.

My contact for card:

Dana Merrow
Founder/CEO
dana@quillmarkledger.example

2740 Harlow Avenue
Boston MA 02135
(617)555-0194

Target Market(s)

Executives, Industry people and investors in the Cannabis sector.

Contact Information for Business Card

PRINTLY does do double sided and the second side can be the same or different images. Only one side is required but use of the second side would be a bonus.

Font styles to use
Serif
Sans Serif
Decorative

Colors

Designer to choose colors to be used in the design.

Requirements
Must have
• Logo, contact info
Nice to have
• Style and design to make the card stand out in a crowd.

```html
<!DOCTYPE html>
<html lang="en">
<head>
<meta charset="utf-8">
<title>Quillmark Ledger — Business Card</title>
<link href="https://fonts.googleapis.com/css2?family=Roboto:wght@400;500;700&display=swap" rel="stylesheet">
<style>
  :root {
    --brand-blue: #1f74bd;
    --brand-green: #6aa632;
    --paper: #ffffff;
    --stage: #5f656a;
    --stage-light: #7c8388;
    --ink-light: #ffffff;
    --pin: #111417;
  }
  html, body {
    margin: 0;
    padding: 0;
    width: 1200px;
    height: 900px;
    overflow: hidden;
  }
  body {
    background: radial-gradient(ellipse at 50% 40%, var(--stage-light), var(--stage) 75%);
    font-family: "Roboto", Arial, sans-serif;
  }
  .sheet {
    position: relative;
    width: 1200px;
    height: 900px;
  }
  .card {
    position: absolute;
    left: 280px;
    width: 640px;
    height: 366px;
    border-radius: 22px;
    overflow: hidden;
    box-shadow: 0 14px 30px rgba(0,0,0,0.35);
  }
  .card--front { top: 60px; }
  .card--back { top: 474px; }
  .card svg { display: block; }
  .wordmark { font-family: "Roboto", Arial, sans-serif; font-weight: 500; }
  .contact { font-family: "Roboto", Arial, sans-serif; font-size: 14px; fill: var(--brand-blue); }
  .address { font-family: "Roboto", Arial, sans-serif; font-size: 15px; fill: var(--ink-light); }
  .name { font-family: "Roboto", Arial, sans-serif; font-weight: 700; font-size: 22px; fill: var(--ink-light); }
  .role { font-family: "Roboto", Arial, sans-serif; font-size: 13px; fill: var(--ink-light); }
</style>
</head>
<body>
<main class="sheet">

  <section class="card card--front" aria-label="Card front">
    <svg width="640" height="366" viewBox="0 0 640 366" xmlns="http://www.w3.org/2000/svg">
      <rect class="card-paper" width="640" height="366" fill="var(--paper)"/>
      <polygon class="card-blue-field" points="120,366 640,60 640,366" fill="var(--brand-blue)"/>
      <polygon class="name-band" role="img" aria-label="Green textured band behind the name"
               points="420,189.5 640,60 640,118 420,247.5" fill="var(--brand-green)"/>

      <g class="brand">
        <rect x="40" y="44" width="30" height="30" fill="var(--brand-green)"/>
        <text class="wordmark" x="82" y="70" font-size="30" fill="var(--brand-blue)">Quillmark Ledger</text>
      </g>

      <g class="contact-list">
        <g class="contact-phone">
          <rect x="40" y="219" width="18" height="18" rx="2" fill="var(--brand-blue)"/>
          <path d="M44 223 q1 -1 2 0 l2 2 q1 1 0 2 l-1 1 q1 3 4 4 l1 -1 q1 -1 2 0 l2 2 q1 1 0 2 l-1 1 q-6 0 -10 -5 q-3 -4 -1 -8z" fill="var(--ink-light)"/>
          <text class="contact" x="66" y="233">(617)555-0194</text>
        </g>
        <g class="contact-email">
          <rect x="40" y="246" width="18" height="18" rx="2" fill="var(--brand-blue)"/>
          <rect x="43" y="250" width="12" height="9" fill="none" stroke="var(--ink-light)" stroke-width="1.3"/>
          <path d="M43 250 l6 5 l6 -5" fill="none" stroke="var(--ink-light)" stroke-width="1.3"/>
          <text class="contact" x="66" y="260">dana@quillmarkledger.example</text>
        </g>
      </g>

      <g class="identity" transform="translate(540 150) rotate(-30.5)">
        <text class="name" x="0" y="-2" text-anchor="middle">Dana Merrow</text>
        <text class="role" x="-6" y="16" text-anchor="middle">Founder/CEO</text>
      </g>

      <g class="address-block">
        <path d="M400 290 a8 8 0 0 1 16 0 c0 6 -8 14 -8 14 s-8 -8 -8 -14z" fill="var(--pin)"/>
        <circle cx="408" cy="290" r="3" fill="var(--brand-blue)"/>
        <text class="address" x="428" y="296">2740 Harlow Avenue</text>
        <text class="address" x="428" y="316">Boston MA 02135</text>
      </g>
    </svg>
  </section>

  <section class="card card--back" aria-label="Card back">
    <svg width="640" height="366" viewBox="0 0 640 366" xmlns="http://www.w3.org/2000/svg">
      <rect class="card-blue-field" width="640" height="366" fill="var(--brand-blue)"/>
      <g class="brand brand--large">
        <rect x="78" y="155" width="52" height="52" fill="var(--ink-light)"/>
        <text class="wordmark" x="148" y="203" font-size="56" fill="var(--ink-light)">Quillmark Ledger</text>
      </g>
    </svg>
  </section>

</main>
</body>
</html>
```